Brisk Sealcraft - Logo and Advert

Help to provide logo and advert.
Advert is to be short and concise to fit in a printed directory posted around homes.
Ideally the same advert to be able to be blown up as a leaflet.
Use of eco friendly type colours, soft greens and blues.
Logo to be subtle but indicative to roofing and facades.
Breakdown of advert as follows;
Company name:
Brisk Sealcraft
Sub title:
Roofing & Façades
Services breakdown:
Pitched (Slating & Tiling)
Flat (Single Ply, Liquid & Mineral Felt)
Hard Metal (Zinc Standing Seam)
Leadwork
Roof lights and lanterns
Generic notes:
100% flame free applications available, eliminating all fire risks to your property. (No gas torch’s etc.).
Expert consultation and advice.
Product warranty and/or insurance backed warranty available.
Fully insured contractor.
Contact information:
Phone number to be confirmed
Email and/or website to be confirmed.
Please feel free to try out different colours and fonts other than outlined. I am not limited to those and open to suggestions.
Updates
Target Market(s)
Domestic/Private Home Owners/Small Buidlers
Industry/Entity Type
Roofing
Font styles to use
Look and feel
Each slider illustrates characteristics of the customer's brand and the style your logo design should communicate.

```html
<!DOCTYPE html>
<html lang="en">
<head>
<meta charset="utf-8">
<title>Brisk Sealcraft – Roofing &amp; Façades</title>
<link href="https://fonts.googleapis.com/css2?family=Nunito:wght@400;500;600;700&display=swap" rel="stylesheet">
<style>
:root{
  --navy:#134b7a;
  --cyan:#00c3de;
  --cyan-line:#4fd3e3;
  --ink:#1f2430;
  --pale-blue:#e6f2fa;
  --pale-aqua:#e3f5f9;
  --white:#ffffff;
}
*{margin:0;padding:0;box-sizing:border-box}
html,body{width:933px;height:1200px;overflow:hidden;background:var(--white)}
body{font-family:'Nunito',sans-serif;color:var(--ink)}
.flyer{position:relative;width:933px;height:1200px;background:var(--white);overflow:hidden}
.shapes{position:absolute;left:0;top:0}
.brand{position:absolute;text-align:center;color:var(--navy);font-weight:600;line-height:1}
.brand .sub{display:block;color:var(--cyan);font-weight:500}
.brand-top{left:24px;width:300px;top:120px;font-size:27px}
.brand-top .sub{font-size:19px;margin-top:10px}
.brand-faint{left:679px;width:223px;top:580px;font-size:19px;color:var(--white);opacity:.9}
.brand-faint .sub{color:var(--white);font-size:13px;margin-top:6px}
.brand-bottom{left:373px;width:300px;top:1058px;font-size:23px}
.brand-bottom .sub{font-size:15px;margin-top:7px}
.promises{position:absolute;left:350px;width:318px;top:44px;text-align:center;color:var(--white);font-size:20px;line-height:36px;font-weight:500}
.services{position:absolute;left:21px;top:980px;color:var(--white)}
.services h2{font-size:23px;font-weight:500;margin-bottom:14px}
.services ul{list-style:none;font-size:16.5px;line-height:29.5px}
.services li::before{content:"•";font-size:13px;margin-right:7px;vertical-align:1px}
.why{position:absolute;right:33px;top:773px;width:420px;text-align:right}
.why h2{color:var(--navy);font-size:23px;font-weight:700;margin-bottom:10px}
.why p{font-size:15.5px;line-height:24px;margin-bottom:11px}
.contact{position:absolute;font-size:12.5px;line-height:19px;color:var(--ink)}
.address{left:449px;top:1122px}
.phone{right:76px;top:1095px;text-align:right}
.email{right:76px;top:1143px;text-align:right}
</style>
</head>
<body>
<div class="flyer">
  <svg class="shapes" width="933" height="1200" viewBox="0 0 933 1200">
    <defs>
      <linearGradient id="lead" x1="0" y1="0" x2="1" y2="1"><stop offset="0" stop-color="#5b6066"/><stop offset=".6" stop-color="#3d4247"/><stop offset="1" stop-color="#d9d6c6"/></linearGradient>
      <linearGradient id="membrane" x1="0" y1="0" x2="1" y2="1"><stop offset="0" stop-color="#eef2f6"/><stop offset=".45" stop-color="#9cc0e2"/><stop offset="1" stop-color="#4c86c4"/></linearGradient>
      <linearGradient id="zinc" x1="0" y1="0" x2="1" y2="1"><stop offset="0" stop-color="#8e9296"/><stop offset="1" stop-color="#5f6469"/></linearGradient>
      <linearGradient id="lantern" x1="0" y1="0" x2="0" y2="1"><stop offset="0" stop-color="#2f5fa8"/><stop offset=".5" stop-color="#8fa8c4"/><stop offset="1" stop-color="#3b4148"/></linearGradient>
      <linearGradient id="tiles" x1="0" y1="0" x2="0" y2="1"><stop offset="0" stop-color="#5c646c"/><stop offset=".6" stop-color="#7a7f84"/><stop offset="1" stop-color="#9a5a45"/></linearGradient>
    </defs>
    <polygon points="350,0 711,0 711,167 509,242 350,167" fill="var(--navy)"/>
    <polyline points="681,0 681,177 853,269 933,226" fill="none" stroke="var(--cyan-line)" stroke-width="4"/>
    <polygon role="img" aria-label="Zinc standing seam roof panels" points="699,0 933,0 933,210 855,249 699,167" fill="url(#zinc)"/>
    <polygon points="0,204 144,278 144,439 0,512" fill="var(--cyan)"/>
    <polygon role="img" aria-label="Welded leadwork flashing" points="178,278 336,198 489,278 489,436 336,515 178,436" fill="url(#lead)"/>
    <polygon role="img" aria-label="Waterproof membrane roll with water droplets" points="524,278 679,198 835,278 835,436 679,515 524,436" fill="url(#membrane)"/>
    <polyline points="0,518 157,452 329,540 329,714 0,874" fill="none" stroke="var(--cyan-line)" stroke-width="4"/>
    <polygon role="img" aria-label="Glass roof lantern under blue sky" points="0,547 159,467 311,543 311,709 0,856" fill="url(#lantern)"/>
    <polygon role="img" aria-label="Tiled pitched roof over brick gable" points="350,546 506,467 661,546 661,704 506,783 350,704" fill="url(#tiles)"/>
    <polygon points="679,533 791,477 902,533 902,648 791,704 679,648" fill="var(--pale-blue)"/>
    <polygon points="283,802 395,747 506,802 506,917 395,973 283,917" fill="var(--pale-aqua)"/>
    <polygon points="0,906 112,839 392,977 392,1200 0,1200" fill="var(--navy)"/>
    <circle cx="425" cy="1140" r="17" fill="none" stroke="var(--cyan-line)" stroke-width="1.2"/>
    <path d="M425 1148c-5-6-7-9-7-12a7 7 0 0 1 14 0c0 3-2 6-7 12z" fill="none" stroke="var(--navy)" stroke-width="1.3"/>
    <circle cx="425" cy="1136" r="2.4" fill="none" stroke="var(--navy)" stroke-width="1.2"/>
    <circle cx="882" cy="1099" r="17" fill="none" stroke="var(--cyan-line)" stroke-width="1.2"/>
    <path d="M876 1091c-2 1-3 3-2 6 2 5 6 9 11 11 3 1 5 0 6-2l-3-3-2 2c-3-1-6-4-7-7l2-2z" fill="none" stroke="var(--navy)" stroke-width="1.2"/>
    <circle cx="882" cy="1151" r="17" fill="none" stroke="var(--cyan-line)" stroke-width="1.2"/>
    <path d="M873 1147v10h18v-10l-9-6z M873 1147l9 6 9-6" fill="none" stroke="var(--navy)" stroke-width="1.2"/>
  </svg>

  <div class="brand brand-top">Brisk Sealcraft<span class="sub">Roofing &amp; Façades</span></div>

  <div class="promises">
    <p>Local Owned &amp; Operated</p>
    <p>Professional Service</p>
    <p>Affordable Rates</p>
  </div>

  <div class="brand brand-faint">Brisk Sealcraft<span class="sub">Roofing &amp; Façades</span></div>

  <section class="why">
    <h2>Why Choose Us</h2>
    <p>100% Flame Free Applications Available,<br>Eliminating All Fire Risks To Your Property</p>
    <p>Expert Consultation And Advice</p>
    <p>Product Warranty And/or Insurance<br>Backed Warranty Available</p>
    <p>Fully Insured Contractor</p>
  </section>

  <section class="services">
    <h2>Our Services</h2>
    <ul>
      <li>Pitched (Slating &amp; Tiling)</li>
      <li>Flat (Single Ply, Liquid &amp; Mineral Felt)</li>
      <li>Hard Metal (Zinc Standing Seam)</li>
      <li>Leadwork</li>
      <li>Roof Lights And Lanterns</li>
    </ul>
  </section>

  <div class="brand brand-bottom">Brisk Sealcraft<span class="sub">Roofing &amp; Façades</span></div>

  <div class="contact address">Street Name, City Name<br>State Zipcode</div>
  <div class="contact phone">555-010-2847</div>
  <div class="contact email">hello@brisksealcraft.com</div>
</div>
</body>
</html>
```